Design a Flooring flyer based on out information

We are a flooring company who specialise in supply & installation of high quality flooring (Laminate, SPC vinyl planks and engineered timber)

The colours in flyer should only consist the same colours in business logo as attached

Flyer needs to show customers we offer samples for free delivered to see quality and colours. This can only be ordered via our website.

Contact number: 1300 482 915

www.breltonsflooringsolutions.com.au

instagram: breltonssolutionsgroup

Inregards to texts for flyer.. I will attach our body content of 'about us' Please add some key points in flyer

About Us

Marcus Brelton founded Brelton’s Flooring Solutions with one goal in mind – quality flooring equipment. Our team is made up of flooring professionals who have had extensive experience with flooring installation themselves. Therefore, we are experts at equipping customers with the right products they need to succeed.

The team at Brelton’s Flooring Solutions have had mastered all sorts of flooring technology as we are always focused on innovation and advancement. For example, our expert team has mastered the correct click system that floors need to be suitable for water spills, surface scratches, and foot traffic impact. This is just one of the ways our hands-on team strives to provide our customers with the innovative flooring technology.

Additionally, we make sure that our products are specifically suited to flourish in the Australian environment, and all of our equipment have been approved by Australian standards. Rain, drought or shine, our products are built to survive in Australian weather.

At Brelton’s Flooring Solutions, we work with you to ensure the best outcome for your unique situation. Just contact our friendly and knowledgeable team today to find out more.

Target Market(s)

Home owners

Requirements
Must have
• Logo colours, modern and expensive

```html
<!DOCTYPE html>
<html lang="en">
<head>
<meta charset="utf-8">
<title>Brelton’s Flooring Solutions – Flyer</title>
<link href="https://fonts.googleapis.com/css2?family=Lato:wght@400;700&display=swap" rel="stylesheet">
<style>
  :root {
    --green: #7dc242;
    --charcoal: #4a4a4a;
    --ink: #2f2f2f;
    --white: #ffffff;
    --page: #e9e9e9;
  }
  * { box-sizing: border-box; margin: 0; padding: 0; }
  html, body { width: 1200px; height: 1200px; overflow: hidden; background: var(--page); }
  body { font-family: 'Lato', sans-serif; color: var(--ink); }

  .flyer {
    position: relative;
    width: 1200px; height: 1200px;
    background: var(--white);
    display: grid;
    grid-template-columns: repeat(4, 300px);
    grid-template-rows: repeat(4, 220px) 180px 140px;
  }

  .photo { width: 100%; height: 100%; }
  .photo--levelling  { background: linear-gradient(135deg, #8a9199 0%, #c9a98a 55%, #5b6168 100%); }
  .photo--oak-floor  { background: linear-gradient(160deg, #f2efe9 0%, #cbb496 60%, #b89c7a 100%); }
  .photo--grain      { background: linear-gradient(135deg, #c99a66 0%, #d8b488 50%, #b8875a 100%); }
  .photo--interior   { background: linear-gradient(180deg, #8e9291 0%, #a3a6a5 60%, #b9b3a8 100%); }
  .photo--living     { background: linear-gradient(170deg, #f4f4f2 0%, #dcdcda 55%, #c9c7c3 100%); }
  .photo--installing { background: linear-gradient(140deg, #f1efeb 0%, #e2cfae 55%, #c8a27f 100%); }
  .photo--samples    { background: linear-gradient(160deg, #6b5a4d 0%, #a99a8c 50%, #4f433b 100%); }
  .photo--sheepskin  { background: linear-gradient(135deg, #8c7a66 0%, #e9e1d2 50%, #a38b72 100%); }

  .block { width: 100%; height: 100%; }
  .block--green { background: var(--green); }
  .block--charcoal { background: var(--charcoal); }

  .samples-note {
    background: var(--charcoal);
    color: var(--white);
    padding: 48px 30px 0 40px;
    font-size: 21px;
    line-height: 1.2;
  }
  .samples-note p + p { margin-top: 18px; }

  .intro-note {
    background: var(--green);
    color: var(--ink);
    padding: 38px 24px 0 30px;
    font-size: 21px;
    line-height: 1.22;
  }

  .about {
    grid-column: 3 / 5;
    grid-row: 2 / 4;
    background: var(--white);
    padding: 28px 34px 0 34px;
    text-align: center;
  }
  .brand {
    display: inline-flex; align-items: center; gap: 12px;
    font-size: 26px; font-weight: 700; color: var(--charcoal);
    letter-spacing: 0.5px;
  }
  .brand__square { width: 22px; height: 22px; background: var(--green); }
  .about__title {
    margin-top: 16px;
    font-size: 26px; font-weight: 700; color: var(--charcoal);
  }
  .about__body {
    margin-top: 12px;
    text-align: left;
    font-size: 12.4px;
    line-height: 1.38;
    color: var(--ink);
  }
  .about__body p + p { margin-top: 7px; }

  .closing {
    grid-column: 1 / 5;
    grid-row: 5;
    background: var(--white);
    padding: 52px 60px 0 60px;
    font-size: 25px;
    line-height: 1.35;
  }

  .contact {
    grid-column: 1 / 5;
    grid-row: 6;
    background: var(--green);
    display: flex; align-items: center; justify-content: center;
    gap: 34px;
    font-size: 24px;
    color: var(--ink);
  }
  .contact__divider { font-size: 26px; }
</style>
</head>
<body>
<main class="flyer">
  <!-- Row 1 -->
  <div class="photo photo--levelling" role="img" aria-label="Gloved hands checking a floor tile with a red spirit level"></div>
  <div class="photo photo--oak-floor" role="img" aria-label="Light oak floor meeting a white skirting board"></div>
  <div class="photo photo--grain" role="img" aria-label="Textured timber boards with a spilled bowl of hazelnuts"></div>
  <div class="block block--green"></div>

  <!-- Row 2 -->
  <div class="samples-note">
    <p>We offer samples for FREE DELIVERED TO SEE QUALITY AND COLOURS.</p>
    <p>This can only be ordered via our website.</p>
  </div>
  <div class="photo photo--interior" role="img" aria-label="Grey room with timber slat wall, pendant lights and a chair"></div>

  <section class="about">
    <div class="brand"><span class="brand__square"></span>Brelton’s Solutions Group</div>
    <h2 class="about__title">About Us</h2>
    <div class="about__body">
      <p>Marcus Brelton founded Brelton’s Flooring Solutions with one goal in mind – quality flooring equipment. Our team is made up of flooring professionals who have had extensive experience with flooring installation themselves. Therefore, we are experts at equipping customers with the right products they need to succeed.</p>
      <p>The team at Brelton’s Flooring Solutions have had mastered all sorts of flooring technology as we are always focused on innovation and advancement. For example, our expert team has mastered the correct click system that floors need to be suitable for water spills, surface scratches, and foot traffic impact. This is just one of the ways our hands-on team strives to provide our customers with the innovative flooring technology.</p>
      <p>Additionally, we make sure that our products are specifically suited to flourish in the Australian environment, and all of our equipment have been approved by Australian standards. Rain, drought or shine, our products are built to survive in Australian weather.</p>
    </div>
  </section>

  <!-- Row 3 -->
  <div class="photo photo--living" role="img" aria-label="Bright living room with pale laminate floor and a dark sofa"></div>
  <div class="intro-note">
    <p>We are a flooring company who specialise in supply &amp; installation of high quality flooring (Laminate, SPC vinyl planks and engineered timber)</p>
  </div>

  <!-- Row 4 -->
  <div class="photo photo--installing" role="img" aria-label="Hands laying a laminate plank over underlay"></div>
  <div class="photo photo--samples" role="img" aria-label="Stacked vinyl plank samples in brown and grey tones"></div>
  <div class="block block--charcoal"></div>
  <div class="photo photo--sheepskin" role="img" aria-label="Sheepskin rug with a book and a cup on a timber floor"></div>

  <!-- Footer -->
  <section class="closing">
    <p>At Brelton’s Flooring Solutions, we work with you to ensure the best outcome for your unique situation.<br>Just contact our friendly and knowledgeable team today to find out more.</p>
  </section>
  <footer class="contact">
    <span>1300 482 915</span>
    <span class="contact__divider">|</span>
    <span>www.breltonsflooringsolutions.com.au</span>
    <span class="contact__divider">|</span>
    <span>breltonssolutionsgroup</span>
  </footer>
</main>
</body>
</html>
```